Webbanner-Design für Informatik Dienstleistungen und Webdesign
Zielgruppe
Informatik Dienstleistungen und Webdesign
Aufgabenstellung
Es soll immer das gleiche Gesicht auf den Banner und ein kurzer Satz.
1. Sie haben das Business - wir die Software
2. Sie haben Anforderungen - wir Lösungen
3. Sie brauchen Unterstützung - wir helfen
Die Banner sollen auf unserer Homepage www.varmek-design.ch auf der Startseite durchlaufen. Das Format soll 1200x500 Pixel sein

```html
<!DOCTYPE html>
<html lang="de">
<head>
<meta charset="utf-8">
<title>Banner – Sie haben das Business, wir die Software</title>
<link rel="stylesheet" href="https://fonts.googleapis.com/css2?family=Noto+Sans:wght@400&display=swap">
<style>
  :root {
    --navy-deep: #02060b;
    --navy: #061423;
    --blue-mid: #0d3f66;
    --blue-glow: #1f8fd0;
    --blue-light: #6fd2fa;
    --cyan-bright: #a8e8ff;
    --text-white: #ffffff;
    --text-accent: #47b9ee;
    --portrait-dark: #0c0f13;
    --portrait-shirt: #15181c;
    --portrait-skin: #b88a68;
    --portrait-hair: #8f7456;
  }
  * { margin: 0; padding: 0; box-sizing: border-box; }
  html, body {
    width: 1200px;
    height: 500px;
    overflow: hidden;
    background: var(--navy-deep);
  }
  .banner {
    position: relative;
    width: 1200px;
    height: 500px;
    overflow: hidden;
    background: linear-gradient(90deg, var(--navy-deep) 0%, var(--navy) 25%, #0a2a46 45%, #0d3d63 70%, #0b3556 100%);
    font-family: "Noto Sans", sans-serif;
  }
  .tech-backdrop {
    position: absolute;
    inset: 0;
    background:
      radial-gradient(ellipse 260px 200px at 1010px 150px, rgba(168,232,255,0.55), transparent 70%),
      radial-gradient(ellipse 420px 320px at 1000px 200px, rgba(111,210,250,0.45), transparent 72%),
      radial-gradient(ellipse 240px 220px at 560px 240px, rgba(111,210,250,0.45), transparent 70%),
      radial-gradient(ellipse 380px 320px at 520px 200px, rgba(31,143,208,0.5), transparent 72%),
      radial-gradient(ellipse 260px 160px at 620px 20px, rgba(111,210,250,0.35), transparent 70%),
      radial-gradient(ellipse 300px 220px at 1130px 420px, rgba(31,143,208,0.45), transparent 70%),
      radial-gradient(ellipse 220px 200px at 430px 420px, rgba(13,63,102,0.6), transparent 70%),
      radial-gradient(ellipse 220px 260px at 60px 240px, rgba(13,63,102,0.45), transparent 70%);
  }
  .portrait {
    position: absolute;
    left: 500px;
    top: 0;
    width: 560px;
    height: 500px;
    background:
      radial-gradient(ellipse 95px 130px at 255px 185px, var(--portrait-skin), transparent 80%),
      radial-gradient(ellipse 190px 260px at 270px 210px, var(--portrait-hair), transparent 78%),
      linear-gradient(180deg, transparent 0%, transparent 55%, var(--portrait-shirt) 72%, var(--portrait-dark) 100%);
    -webkit-mask-image: radial-gradient(ellipse 300px 520px at 280px 300px, #000 70%, transparent 100%);
    mask-image: radial-gradient(ellipse 300px 520px at 280px 300px, #000 70%, transparent 100%);
  }
  .claims {
    position: absolute;
    left: 28px;
    top: 48px;
    list-style: none;
  }
  .claim { margin-bottom: 42px; }
  .claim-lead {
    display: block;
    color: var(--text-white);
    font-size: 22.5px;
    line-height: 26px;
  }
  .claim-answer {
    display: block;
    color: var(--text-accent);
    font-size: 33.5px;
    line-height: 40px;
    letter-spacing: 0.3px;
    text-transform: uppercase;
  }
</style>
</head>
<body>
  <main class="banner">
    <div class="tech-backdrop" role="img" aria-label="Leuchtende blaue Leiterbahnen mit Symbolen für Team, Zeit, Statistik, Zahnräder und Monitor"></div>
    <div class="portrait" role="img" aria-label="Porträtfoto einer lächelnden jungen Frau mit langen blonden Haaren im schwarzen Firmen-Shirt"></div>
    <ul class="claims">
      <li class="claim">
        <span class="claim-lead">Sie haben das Business</span>
        <span class="claim-answer">Wir die Software</span>
      </li>
      <li class="claim">
        <span class="claim-lead">Sie haben Anforderungen</span>
        <span class="claim-answer">Wir Lösungen</span>
      </li>
      <li class="claim">
        <span class="claim-lead">Sie brauchen Unterstützung</span>
        <span class="claim-answer">Wir helfen</span>
      </li>
    </ul>
  </main>
</body>
</html>
```